Equestrian business web design and build

I have secured a Pixel Harbor account and started roughly working through a website, but I need help adding functionality and formatting content. I had Motif Hive create a logo for me and now I am at the next step.

Target Market(s)

hunter jumper equestrian community

Industry/Entity Type

equestrian

Coding

Coded - Design and coding required

Font styles to use
Other font styles liked:
• Stranger wide is the font

Requirements
Must have
• Lots of high rez photos, embedded video, charts

```html
<!DOCTYPE html>
<html lang="en">
<head>
<meta charset="utf-8">
<title>Azure Paddock</title>
<link href="https://fonts.googleapis.com/css2?family=Krona+One&family=Montserrat:wght@400;500;600&family=Arimo:wght@400;700&display=swap" rel="stylesheet">
<style>
:root{
  --white:#ffffff;
  --ink:#2b2b2b;
  --body:#6f6f6f;
  --navy:#24296b;
  --blue:#3572b0;
  --footer:#24286a;
  --outline:#2f4a96;
  --icon:#1a1e55;
}
*{margin:0;padding:0;box-sizing:border-box}
html,body{width:1200px;height:3805px;overflow:hidden;background:var(--white)}
body{position:relative;font-family:"Montserrat",sans-serif;color:var(--body)}
.abs{position:absolute}
.display{font-family:"Krona One",sans-serif;color:var(--ink);letter-spacing:5px;text-align:center;font-weight:400;white-space:nowrap}

.hero{left:0;top:0;width:1200px;height:681px;background:linear-gradient(160deg,#5a6456 0%,#4b5a44 35%,#6b6a5e 60%,#3e4a36 100%)}
.hero-shade{left:0;top:0;width:1200px;height:681px;background:rgba(0,0,0,.25)}
.brand{left:112px;top:50px;display:flex;align-items:center;gap:10px;color:var(--white);font-family:"Montserrat",sans-serif;font-weight:600;font-size:17px;letter-spacing:1px;white-space:nowrap}
.brand-dot{width:14px;height:14px;border-radius:50%;background:var(--white)}
.nav a{position:absolute;top:52px;color:var(--white);font-size:14px;font-weight:600;text-decoration:none;white-space:nowrap}
.nav .current{border-bottom:2px solid var(--white);padding-bottom:5px}
.btn-ghost{display:flex;align-items:center;justify-content:center;border:2px solid var(--white);border-radius:24px;color:var(--white);font-size:14px;font-weight:600}
.hero-title{left:0;top:292px;width:1200px;color:var(--white);font-size:62px;letter-spacing:7px}
.dots{left:563px;top:597px;display:flex;gap:8px}
.dots span{width:12px;height:12px;border-radius:50%;background:rgba(255,255,255,.5)}
.dots span:first-child{background:var(--white)}

.h2{font-size:36px}
.copy{font-size:14px;line-height:25.7px;text-align:center}
.copy.just{text-align:justify;text-align-last:center}
.btn-outline{display:flex;align-items:center;justify-content:center;border:2px solid var(--outline);border-radius:24px;color:var(--navy);font-size:14px;font-weight:600}
.photo{border-radius:4px}

.team-photo{width:232px;height:256px}
.team-name{width:300px;text-align:center;font-family:"Arimo",sans-serif;font-weight:700;font-size:20px;color:#3a3a3a}
.team-role{width:300px;text-align:center;font-family:"Arimo",sans-serif;font-size:13px;color:#555;letter-spacing:.3px}

.subscribe{left:0;top:3229px;width:1200px;height:355px;background:var(--blue)}
.sub-form{left:251px;top:3414px;width:698px;height:68px;background:var(--white);border-radius:4px}
.sub-field{left:24px;top:24px;font-size:16px;color:#777}
.sub-btn{left:546px;top:9px;width:144px;height:50px;background:var(--navy);border-radius:4px;color:var(--white);font-weight:600;font-size:16px;display:flex;align-items:center;justify-content:center}

.footer{left:0;top:3584px;width:1200px;height:221px;background:var(--footer);color:var(--white);text-align:center;font-size:14px}
</style>
</head>
<body>

<header>
  <div class="abs hero" role="img" aria-label="Show jumper clearing a fence in an indoor championship arena with judges behind"></div>
  <div class="abs hero-shade"></div>
  <div class="abs brand"><span class="brand-dot"></span>AZURE PADDOCK</div>
  <nav class="nav">
    <a class="current" style="left:489px">Home</a>
    <a style="left:563px">About</a>
    <a style="left:638px">Kilimanjaro</a>
    <a style="left:752px">Gallery</a>
    <a style="left:835px">Contact</a>
  </nav>
  <div class="abs btn-ghost" style="left:928px;top:38px;width:160px;height:45px">Get in Touch</div>
  <h1 class="abs display hero-title">AZURE PADDOCK</h1>
  <div class="abs btn-ghost" style="left:520px;top:386px;width:160px;height:43px">Get Started</div>
  <div class="abs dots"><span></span><span></span><span></span><span></span></div>
</header>

<section>
  <h2 class="abs display h2" style="left:0;top:778px;width:1200px">WELCOME TO AZURE PADDOCK</h2>
  <p class="abs copy" style="left:225px;top:840px;width:750px">Lorem ipsum dolor sit amet, consectetur adipiscing elit, sed do eiusmod tempor incididunt ut labore et dolore magna aliqua. Ut enim ad minim veniam, quis nostrud exercitation ullamco laboris nisi ut aliquip ex ea commodo consequat.</p>
</section>

<section>
  <div class="abs photo" style="left:129px;top:983px;width:421px;height:396px;background:linear-gradient(180deg,#a9c4d6 0%,#7c9a5c 45%,#6b4a30 75%,#b9a98f 100%)" role="img" aria-label="Rider on a bay horse jumping among palm trees"></div>
  <h2 class="abs display h2" style="left:625px;top:994px;width:448px">ABOUT US</h2>
  <p class="abs copy just" style="left:625px;top:1056px;width:448px">Lorem ipsum dolor sit amet, consectetur adipiscing elit, sed do eiusmod tempor incididunt ut labore et dolore magna aliqua. Ut enim ad minim veniam, quis nostrud exercitation ullamco laboris nisi ut aliquip ex ea commodo consequat. Duis aute irure dolor in reprehenderit in voluptate velit esse cillum dolore eu fugiat nulla pariatur. Excepteur sint occaecat cupidatat non proident, sunt in culpa qui officia deserunt mollit anim id est laborum.Lorem ipsum dolor sit amet, consectetur adipiscing elit, sed do eiusmod tempor incididunt</p>
  <div class="abs btn-outline" style="left:769px;top:1318px;width:159px;height:43px">Learn More</div>

  <h2 class="abs display h2" style="left:129px;top:1465px;width:447px">KILIMANJARO</h2>
  <p class="abs copy just" style="left:129px;top:1527px;width:447px">Lorem ipsum dolor sit amet, consectetur adipiscing elit, sed do eiusmod tempor incididunt ut labore et dolore magna aliqua. Ut enim ad minim veniam, quis nostrud exercitation ullamco laboris nisi ut aliquip ex ea commodo consequat. Duis aute irure dolor in reprehenderit in voluptate velit esse cillum dolore eu fugiat nulla pariatur. Excepteur sint occaecat cupidatat non proident, sunt in culpa qui officia deserunt mollit anim id est laborum.Lorem ipsum dolor sit amet, consectetur adipiscing elit, sed do eiusmod tempor incididunt</p>
  <div class="abs btn-outline" style="left:272px;top:1790px;width:160px;height:43px">Learn More</div>
  <div class="abs photo" style="left:650px;top:1454px;width:423px;height:396px;background:linear-gradient(180deg,#b7cbe0 0%,#8aa56c 35%,#b33a3a 62%,#d8c7a8 100%)" role="img" aria-label="Horse and rider clearing red and white show jump"></div>
</section>

<section>
  <h2 class="abs display h2" style="left:0;top:1988px;width:1200px">GALLERY</h2>
  <div class="abs" style="left:9px;top:2072px;width:384px;height:279px;background:linear-gradient(180deg,#c9d2da 0%,#6b6a4a 50%,#7a7a58 100%)" role="img" aria-label="Jumper under a large spreading oak tree"></div>
  <div class="abs" style="left:408px;top:2072px;width:384px;height:279px;background:linear-gradient(180deg,#4d5f42 0%,#8a5a34 60%,#5f7a48 100%)" role="img" aria-label="Young rider on a chestnut horse over a fence"></div>
  <div class="abs" style="left:807px;top:2072px;width:384px;height:279px;background:linear-gradient(135deg,#8da863 0%,#8b4a26 50%,#c2c6b8 100%)" role="img" aria-label="Close view of a bay horse with braided mane"></div>
  <div class="abs" style="left:9px;top:2363px;width:384px;height:281px;background:linear-gradient(180deg,#6e8a54 0%,#5a3a26 55%,#d6d0c2 100%)" role="img" aria-label="Horse and rider mid jump"></div>
  <div class="abs" style="left:408px;top:2363px;width:384px;height:281px;background:linear-gradient(180deg,#a69c88 0%,#c9c2aa 55%,#6c6a5c 100%)" role="img" aria-label="Dogs riding in a golf cart at the show grounds"></div>
  <div class="abs" style="left:807px;top:2363px;width:384px;height:281px;background:linear-gradient(180deg,#3f5a35 0%,#9aa0a6 60%,#6a4032 100%)" role="img" aria-label="Grey horse jumping in front of a hedge"></div>
</section>

<section>
  <h2 class="abs display h2" style="left:0;top:2735px;width:1200px">OUR TEAM</h2>
  <div class="abs team-photo" style="left:160px;top:2814px;background:linear-gradient(180deg,#cfcac2,#9c8a78)" role="img" aria-label="Portrait of the founder"></div>
  <div class="abs team-photo" style="left:485px;top:2814px;background:linear-gradient(180deg,#d7d4cf,#3e4a42)" role="img" aria-label="Portrait of the design director"></div>
  <div class="abs team-photo" style="left:810px;top:2814px;background:linear-gradient(180deg,#7e9a6a,#2c4a74)" role="img" aria-label="Portrait of the sustainability director"></div>
  <div class="abs team-name" style="left:126px;top:3080px">Nadia Ashford</div>
  <div class="abs team-role" style="left:126px;top:3113px">FOUNDER</div>
  <div class="abs team-name" style="left:451px;top:3080px">Julian Crane</div>
  <div class="abs team-role" style="left:451px;top:3113px">DESIGN DIRECTOR</div>
  <div class="abs team-name" style="left:776px;top:3080px">Mei Lindqvist</div>
  <div class="abs team-role" style="left:776px;top:3113px">SUSTAINABILITY DIRECTOR</div>
</section>

<section class="abs subscribe">
  <h2 class="abs display" style="left:0;top:83px;width:1200px;color:var(--white);font-size:38px">SUBSCRIBE</h2>
  <p class="abs" style="left:0;top:144px;width:1200px;text-align:center;color:var(--white);font-size:16px">Sign up with your email address to receive news and updates.</p>
</section>
<div class="abs sub-form">
  <span class="abs sub-field">Email Address</span>
  <div class="abs sub-btn">Sign Up</div>
</div>

<footer class="abs footer">
  <p class="abs" style="left:0;top:71px;width:1200px">48 Fieldstone Lane, Ocala FL &nbsp;&nbsp;|&nbsp;&nbsp; (555) 014-2736 &nbsp;&nbsp;|&nbsp;&nbsp; hello@azurepaddock.test</p>
  <p class="abs" style="left:0;top:114px;width:1200px">© 2023 Company name. All Rights Reserved.</p>
  <svg class="abs" style="left:588px;top:155px" width="24" height="24" viewBox="0 0 24 24"><circle cx="12" cy="12" r="12" fill="var(--icon)"/></svg>
</footer>

</body>
</html>
```